Create the ONLY Supplement line for Male Entrepreneurs! (Veltro Prime MD)

I need a label designed for a new supplement brand that I am launching.

There are five products so need a design that I can simply change the wording for each individual product

The brand name is called veltro prime MD. The focus is male entrepreneurial health.

Target audience is men 35 to 55.

Concepts: the healthier you are in body the more money you will make in business.

Concept to copy: I want to make a clean minimalistic label mimicking Dallamore MD (google it and you'll see what I mean)

Target Market(s)

male entrepreneurs 35-55

Industry/Entity Type

Health Supplement

Colors

Designer to choose colors to be used in the design.

Requirements
Must have
• Modern classy design, similar to Dallamore MD.
Nice to have
• Highlight that the supplement is Doctor Approved.
Should not have
• No loud colors. Present it as high class.

```html
<!DOCTYPE html>
<html lang="en">
<head>
<meta charset="UTF-8">
<title>Veltro Prime MD – Omega 3 Label</title>
<link href="https://fonts.googleapis.com/css2?family=Bebas+Neue&family=Archivo:wght@400&display=swap" rel="stylesheet">
<style>
  :root {
    --page: #f4f5f8;
    --label: #d5d6cd;
    --label-light: #dfe0d8;
    --ink: #2f2f2f;
    --ink-soft: #4a4a4a;
    --rule: #3a3a3a;
    --band: #2b2b2b;
    --seal: #2d2d2d;
    --seal-line: #9a9a94;
    --seal-mark: #e6e6e0;
  }
  * { margin: 0; padding: 0; box-sizing: border-box; }
  html, body {
    width: 1180px;
    height: 1200px;
    overflow: hidden;
    background: var(--page);
  }
  .label {
    position: absolute;
    left: 180px;
    top: 75px;
    width: 820px;
    height: 1050px;
    background: var(--label);
    color: var(--ink);
  }
  .label__top-strip {
    position: absolute; left: 0; top: 0; width: 100%; height: 24px;
    background: var(--label-light);
  }
  .label__band {
    position: absolute; left: 0; top: 24px; width: 100%; height: 20px;
    background: var(--band);
  }
  .brand-name {
    position: absolute; left: 0; top: 250px; width: 100%;
    text-align: center;
    font-family: "Archivo", sans-serif;
    font-size: 68px; line-height: 1; letter-spacing: 1px;
    color: var(--ink);
  }
  .rule { position: absolute; background: var(--rule); }
  .rule--v { width: 3px; }
  .rule--h { height: 3px; }
  .product-name {
    position: absolute; left: 72px; top: 566px;
    font-family: "Bebas Neue", sans-serif;
    font-size: 132px; line-height: 1; letter-spacing: 4px;
    color: var(--ink);
  }
  .product-claim {
    position: absolute; left: 74px; top: 724px;
    font-family: "Archivo", sans-serif;
    font-size: 31px; line-height: 1; letter-spacing: 0.5px;
    color: var(--ink-soft);
  }
  .count {
    position: absolute; left: 72px; top: 848px; width: 170px;
    text-align: center;
    font-family: "Archivo", sans-serif;
    color: var(--ink-soft);
  }
  .count__number { font-size: 64px; line-height: 1; }
  .count__unit { font-size: 36px; line-height: 1; margin-top: 14px; }
  .product-type {
    position: absolute; left: 272px; top: 878px;
    font-family: "Archivo", sans-serif;
    font-size: 38px; line-height: 48px;
    color: var(--ink-soft);
  }
  .seal {
    position: absolute; left: 569px; top: 683px;
    width: 188px; height: 188px;
  }
</style>
</head>
<body>
  <main class="label">
    <div class="label__top-strip"></div>
    <div class="label__band"></div>

    <h1 class="brand-name">Veltro Prime MD</h1>

    <div class="product-name">OMEGA 3</div>
    <div class="rule rule--v" style="left:519px; top:554px; height:256px;"></div>
    <div class="rule rule--h" style="left:72px; top:681px; width:450px;"></div>
    <div class="product-claim">SUPPORT HEART HEALTH</div>
    <div class="rule rule--h" style="left:72px; top:808px; width:450px;"></div>

    <div class="count">
      <div class="count__number">90</div>
      <div class="count__unit">Capsules</div>
    </div>
    <div class="rule rule--v" style="left:250px; top:838px; height:142px;"></div>
    <div class="product-type">Dietary<br>Supplement</div>
    <div class="rule rule--v" style="left:519px; top:838px; height:142px;"></div>

    <svg class="seal" viewBox="0 0 188 188" role="img" aria-label="Doctor approved seal">
      <circle cx="94" cy="94" r="92" fill="var(--seal)"/>
      <circle cx="94" cy="94" r="80" fill="none" stroke="var(--seal-line)" stroke-width="2"/>
      <circle cx="94" cy="94" r="46" fill="none" stroke="var(--seal-line)" stroke-width="2"/>
      <path d="M74 96 L89 112 L118 72" fill="none" stroke="var(--seal-mark)" stroke-width="6" stroke-linecap="round" stroke-linejoin="round"/>
    </svg>
  </main>
</body>
</html>
```